VALMIKE GROUP

This is a company that provides executive protection. Our motto is "New Era in Protection"... I don't want this to look like other security websites. I want it to be clean and sharp and represent a new era. We are based in the bay area so maybe a picture of San Francisco in the background?
I want it to be able to funnel down a couple different categories.
1. About Us
2. Services (Executive Protection, Covert Protection, Residential Protection & Intelligence)
3. Iron Finch (Training & Consulting)
4. Contact Us
I want it to be very clean and modern. I don't want there to be any pictures of bodyguards with ear pieces like every other website.
Target Market(s)
Ultra High Net Worth Individuals
Coding
Coded - Design and coding required
Number of Pages Required
1 page
Requirements
Must have
- Colors of my Symbol
Nice to have
- City in the background, San Francisco, New York or the Pinehallow Club in Montana.
Should not have
- Should not look like an KVM website or have photos of bodyguards. I want this to be a clean and simple website with my logo

```html
<!DOCTYPE html>
<html lang="en">
<head>
<meta charset="utf-8">
<title>VALMIKE GROUP – New Era in Protection</title>
<link href="https://fonts.googleapis.com/css2?family=Orbitron:wght@600;700&family=Poppins:ital,wght@0,400;0,500;1,400&family=Oswald:wght@500&display=swap" rel="stylesheet">
<style>
:root{
  --red:#8b151b;
  --red-deep:#5e0c10;
  --red-bright:#c4262d;
  --black:#000;
  --ink:#111;
  --white:#fff;
}
*{margin:0;padding:0;box-sizing:border-box}
html,body{width:1200px;height:3438px;overflow:hidden}
body{position:relative;background:var(--white);font-family:'Poppins',sans-serif;color:var(--white)}
.stage{position:absolute;left:0;top:0}
.display{font-family:'Orbitron',sans-serif;font-weight:700;letter-spacing:1px}

/* header */
.topbar-text{position:absolute;top:3px;font-family:'Orbitron',sans-serif;font-size:11px;font-weight:600;letter-spacing:.5px;display:flex;align-items:center;gap:5px}
.topbar-mail{left:692px;color:var(--white)}
.topbar-phone{left:905px;color:var(--ink)}
.brand{position:absolute;left:152px;top:24px;display:flex;align-items:center;gap:14px}
.brand-mark{width:52px;height:52px;border-radius:50%;background:var(--red)}
.brand-name{font-family:'Orbitron',sans-serif;font-weight:700;font-size:26px;line-height:1;color:var(--white);letter-spacing:1px}
.nav{position:absolute;top:56px;left:0;width:1200px;font-family:'Oswald',sans-serif;font-size:12px;letter-spacing:.3px}
.nav a{position:absolute;color:var(--white);text-decoration:none;white-space:nowrap}
.nav a.active{color:var(--red-bright)}

.hero-badge{position:absolute;left:496px;top:421px;width:208px;height:208px;border-radius:50%;background:var(--black);display:flex;align-items:center;justify-content:center}
.hero-badge span{font-family:'Orbitron',sans-serif;font-weight:700;color:var(--white);font-size:22px;letter-spacing:1px}

/* about */
.about-title{position:absolute;top:690px;left:0;width:1200px;text-align:center;font-size:22px}
.about-text{position:absolute;top:726px;left:150px;width:900px;text-align:center;font-size:16.5px;line-height:26px;font-weight:400}

/* services */
.services-title{position:absolute;top:1072px;left:0;width:1200px;text-align:center;font-size:22px}
.card{position:absolute;top:1132px;width:276px}
.card-photo{height:228px}
.card-title{margin-top:22px;min-height:44px;text-align:center;color:var(--red-bright);font-family:'Orbitron',sans-serif;font-weight:600;font-size:15.5px;line-height:22px;letter-spacing:.8px}
.card-text{margin-top:12px;font-size:16.5px;line-height:26px;text-align:justify;hyphens:auto}
.btn{display:block;background:var(--red);color:var(--white);font-size:16px;text-align:center;border-radius:16px;text-decoration:none}
.card .btn{width:143px;height:30px;line-height:30px;margin:16px auto 0}

/* iron finch */
.finch-title{position:absolute;top:1884px;right:152px;font-size:22px}
.finch-text{position:absolute;top:1931px;right:152px;width:500px;text-align:right;font-size:16px;line-height:26px;hyphens:auto}
.finch-list{position:absolute;top:2141px;right:152px;list-style:none}
.finch-list li{display:flex;justify-content:flex-end;align-items:center;gap:15px;height:35.3px;font-style:italic;font-size:16.5px}

/* contact */
.contact-title{position:absolute;top:2486px;left:0;width:1200px;text-align:center;color:var(--ink);font-size:24px}
.contact-sub{position:absolute;top:2527px;left:0;width:1200px;text-align:center;color:var(--ink);font-size:14px}
.field{position:absolute;border:1.5px solid var(--red);border-radius:20px;color:#333;font-size:15px;padding:8px 22px}
.contact-form .btn{position:absolute;left:534px;top:2765px;width:132px;height:35px;line-height:35px}
.map{position:absolute;left:0;top:2833px;width:1200px;height:420px;
  background:
    radial-gradient(ellipse 260px 120px at 130px 330px,rgba(160,200,235,.55),transparent 70%),
    radial-gradient(ellipse 420px 60px at 620px 140px,rgba(246,214,120,.45),transparent 70%),
    radial-gradient(ellipse 500px 70px at 900px 250px,rgba(246,214,120,.4),transparent 70%),
    radial-gradient(ellipse 160px 90px at 1120px 240px,rgba(190,225,190,.55),transparent 70%),
    linear-gradient(135deg,#eef0f2,#e6e9ec 55%,#eef0ec)}

/* footer */
.footer{position:absolute;left:0;top:3253px;width:1200px;height:164px;background:var(--black)}
.footer-brand{position:absolute;left:150px;top:36px;text-align:center}
.footer-brand .brand-mark{width:34px;height:34px;margin:0 auto 8px}
.footer-brand .brand-name{font-size:16px}
.footer-col{position:absolute;top:34px;font-size:10px;line-height:17.5px}
.footer-col h4{font-family:'Orbitron',sans-serif;font-weight:700;font-size:12px;letter-spacing:.8px;margin-bottom:6px}
.footer-col li{list-style:none}
.social{position:absolute;left:912px;top:111px;display:flex;gap:10px}
.social span{width:23px;height:23px;border:1.5px solid var(--white);border-radius:50%}
.legal{position:absolute;left:0;top:3417px;width:1200px;height:21px;background:var(--red);text-align:center;font-size:9px;line-height:21px}
</style>
</head>
<body>

<svg class="stage" width="1200" height="3438" viewBox="0 0 1200 3438">
  <defs>
    <linearGradient id="sky" x1="0" y1="0" x2="0" y2="1">
      <stop offset="0" stop-color="#2a3a55"/>
      <stop offset=".18" stop-color="#56708f"/>
      <stop offset=".32" stop-color="#2f5f86"/>
      <stop offset=".5" stop-color="#23303f"/>
      <stop offset=".75" stop-color="#3a2a22"/>
      <stop offset="1" stop-color="#1c1614"/>
    </linearGradient>
    <radialGradient id="sun" cx="810" cy="175" r="260" gradientUnits="userSpaceOnUse">
      <stop offset="0" stop-color="#ffd27a" stop-opacity=".95"/>
      <stop offset=".3" stop-color="#f09a45" stop-opacity=".6"/>
      <stop offset="1" stop-color="#f09a45" stop-opacity="0"/>
    </radialGradient>
    <radialGradient id="bay" cx="260" cy="250" r="330" gradientUnits="userSpaceOnUse">
      <stop offset="0" stop-color="#3f8ec0" stop-opacity=".8"/>
      <stop offset="1" stop-color="#3f8ec0" stop-opacity="0"/>
    </radialGradient>
    <radialGradient id="lights1" cx="150" cy="560" r="300" gradientUnits="userSpaceOnUse">
      <stop offset="0" stop-color="#e0822e" stop-opacity=".7"/>
      <stop offset="1" stop-color="#e0822e" stop-opacity="0"/>
    </radialGradient>
    <radialGradient id="lights2" cx="1000" cy="430" r="260" gradientUnits="userSpaceOnUse">
      <stop offset="0" stop-color="#c9783a" stop-opacity=".5"/>
      <stop offset="1" stop-color="#c9783a" stop-opacity="0"/>
    </radialGradient>
    <linearGradient id="room" x1="0" y1="0" x2="1" y2="1">
      <stop offset="0" stop-color="#e4e8eb"/>
      <stop offset=".35" stop-color="#c9ced3"/>
      <stop offset=".6" stop-color="#8a8f96"/>
      <stop offset=".8" stop-color="#6a3a2c"/>
      <stop offset="1" stop-color="#2a2526"/>
    </linearGradient>
  </defs>

  <rect x="0" y="0" width="1200" height="88" fill="#111"/>
  <polygon points="676,0 890,0 880,20 666,20" fill="var(--red)"/>
  <polygon points="890,0 1048,0 1038,20 880,20" fill="#fff"/>

  <g role="img" aria-label="City skyline at dusk overlooking a harbour">
    <rect x="0" y="88" width="1200" height="580" fill="url(#sky)"/>
    <rect x="0" y="88" width="1200" height="580" fill="url(#bay)"/>
    <rect x="0" y="88" width="1200" height="580" fill="url(#sun)"/>
    <rect x="0" y="88" width="1200" height="580" fill="url(#lights1)"/>
    <rect x="0" y="88" width="1200" height="580" fill="url(#lights2)"/>
  </g>

  <polygon points="0,655 480,545 720,545 1200,655 1200,925 0,1101" fill="var(--red)"/>
  <circle cx="590" cy="532" r="104" fill="var(--red-deep)"/>

  <polygon points="0,1101 1200,921 1200,1870 0,1870" fill="var(--black)"/>
  <circle cx="600" cy="1015" r="40" fill="none" stroke="#fff" stroke-width="3"/>
  <circle cx="600" cy="1015" r="33" fill="#fff"/>
  <path d="M600 992 l17 6 v13 c0 12 -8 20 -17 24 c-9 -4 -17 -12 -17 -24 v-13z" fill="var(--black)"/>
  <circle cx="609" cy="1022" r="9" fill="#fff"/>
  <path d="M604 1022 l4 4 l6 -7" stroke="var(--black)" stroke-width="2.5" fill="none"/>

  <polygon points="560,1772 1200,1856 1200,2343 0,2497 0,1731" fill="var(--red)"/>
  <polygon points="0,1731 615,1776 247,2430 0,2296" fill="url(#room)" role="img" aria-label="Trainer presenting to a seated group in a bright meeting room"/>
</svg>

<header>
  <div class="topbar-text topbar-mail">
    <svg width="10" height="10" viewBox="0 0 10 10"><rect x="1" y="2" width="8" height="6" fill="none" stroke="#fff"/><path d="M1 2 l4 3 l4 -3" stroke="#fff" fill="none"/></svg>
    INFO@VALMIKEGROUP.COM
  </div>
  <div class="topbar-text topbar-phone">
    <svg width="10" height="10" viewBox="0 0 10 10"><path d="M2 1 l2 0 l1 2 l-1 1 c1 2 2 3 3 3 l1 -1 l2 1 l0 2 c-5 0 -8 -3 -8 -8z" fill="#111"/></svg>
    555-014-7612
  </div>
  <div class="brand">
    <span class="brand-mark"></span>
    <span class="brand-name">VALMIKE GROUP</span>
  </div>
  <nav class="nav">
    <a href="#about" style="left:769px">ABOUT US</a>
    <a href="#services" style="left:841px">SERVICES</a>
    <a href="#iron-finch" class="active" style="left:916px">IRON FINCH</a>
    <a href="#contact" style="left:989px">CONTACT US</a>
  </nav>
</header>

<div class="hero-badge"><span>VALMIKE</span></div>

<section id="about">
  <h2 class="about-title display">ABOUT US</h2>
  <p class="about-text">Lorem ipsum dolor sit amet, consectetur adipiscing elit, sed do eiusmod tempor incididunt ut labore et dolore magna aliqua. Quis ipsum suspendisse ultrices gravida. Risus commodo viverra maecenas accumsan lacus vel facilisis. Lorem ipsum dolor sit amet, consectetur adipiscing elit, sed do eiusmod tempor incididunt ut labore et dolore magna aliqua. Quis ipsum suspendisse ultrices gravida. Risus commodo viverra maecenas accumsan lacus vel facilisis. Lorem ipsum dolor sit amet, consectetur adipiscing elit, sed do eiusmod tempor incididunt ut labore et dolore magna aliqua. Quis ipsum suspendisse ultrices gravida. Risus commodo viverra maecenas accumsan lacus vel facilisis.</p>
</section>

<section id="services">
  <h2 class="services-title display">SERVICES</h2>

  <article class="card" style="left:152px">
    <div class="card-photo" role="img" aria-label="Security officer outdoors speaking into a radio" style="background:radial-gradient(ellipse 120px 110px at 170px 70px,#b89a84,transparent 70%),linear-gradient(170deg,#e8eaea 0%,#b9c0c4 30%,#5a636d 60%,#14181f 100%)"></div>
    <h3 class="card-title">EXECUTIVE PROTECTION</h3>
    <p class="card-text">Lorem ipsum dolor sit amet, consectetur adipiscing elit, sed do eiusmod tempor incididunt ut labore et dolore magna aliqua. Quis ipsum suspendisse ultrices gravida. Risus commodo viverra maecenas accumsan lacus vel facilisis. Lorem ipsum dolor sit amet, consectetur adipiscing elit,</p>
    <a class="btn" href="#">Read more</a>
  </article>

  <article class="card" style="left:463px">
    <div class="card-photo" role="img" aria-label="Man in a dark suit beside a black car" style="background:radial-gradient(ellipse 90px 160px at 215px 170px,#1b1c1f,transparent 75%),radial-gradient(ellipse 80px 30px at 60px 130px,#2b2d31,transparent 75%),linear-gradient(180deg,#e4e5e6 0%,#c9cbcd 45%,#9da0a4 75%,#6f7276 100%)"></div>
    <h3 class="card-title">COVERT PROTECTION</h3>
    <p class="card-text">Lorem ipsum dolor sit amet, consectetur adipiscing elit, sed do eiusmod tempor incididunt ut labore et dolore magna aliqua. Quis ipsum suspendisse ultrices gravida. Risus commodo viverra maecenas accumsan lacus vel facilisis. Lorem ipsum dolor sit amet, consectetur adipiscing elit,</p>
    <a class="btn" href="#">Read more</a>
  </article>

  <article class="card" style="left:770px">
    <div class="card-photo" role="img" aria-label="Hands holding an umbrella over a paper house, car and family" style="background:radial-gradient(ellipse 110px 35px at 140px 70px,#7a5d80,transparent 75%),radial-gradient(ellipse 140px 50px at 140px 185px,#fafafa,transparent 75%),linear-gradient(180deg,#1f2838 0%,#2e3850 45%,#8c8f98 75%,#e8e8ea 100%)"></div>
    <h3 class="card-title">RESIDENTIAL PROTECTION &amp; INTELLIGENCE</h3>
    <p class="card-text">Lorem ipsum dolor sit amet, consectetur adipiscing elit, sed do eiusmod tempor incididunt ut labore et dolore magna aliqua. Quis ipsum suspendisse ultrices gravida. Risus commodo viverra maecenas accumsan lacus vel facilisis. Lorem ipsum dolor sit amet, consectetur adipiscing elit,</p>
    <a class="btn" href="#">Read more</a>
  </article>
</section>

<section id="iron-finch">
  <h2 class="finch-title display">IRON FINCH</h2>
  <p class="finch-text">Lorem ipsum dolor sit amet, consectetur adipiscing elit, sed do eiusmod tempor incididunt ut labore et dolore magna aliqua. Quis ipsum suspendisse ultrices gravida. Risus commodo viverra maecenas accumsan lacus vel facilisis. Lorem ipsum dolor sit amet, consectetur adipiscing elit, sed do eiusmod Lorem ipsum dolor sit amet, consectetur adipiscing elit, sed do eiusmod tempor incididunt ut</p>
  <ul class="finch-list">
    <li>consectetur adipiscing eli <svg width="22" height="22" viewBox="0 0 22 22"><circle cx="11" cy="11" r="11" fill="#fff"/><path d="M6 11 l3.5 3.5 l6.5 -7" stroke="#8b151b" stroke-width="2.6" fill="none"/></svg></li>
    <li>Lorem ipsum dolor sit amet, consectetur adipiscing eli <svg width="22" height="22" viewBox="0 0 22 22"><circle cx="11" cy="11" r="11" fill="#fff"/><path d="M6 11 l3.5 3.5 l6.5 -7" stroke="#8b151b" stroke-width="2.6" fill="none"/></svg></li>
    <li>ipsum dolor sit amet, consectetur adipiscing eli <svg width="22" height="22" viewBox="0 0 22 22"><circle cx="11" cy="11" r="11" fill="#fff"/><path d="M6 11 l3.5 3.5 l6.5 -7" stroke="#8b151b" stroke-width="2.6" fill="none"/></svg></li>
    <li>Lorem ipsum dolor sit amet, consectetur <svg width="22" height="22" viewBox="0 0 22 22"><circle cx="11" cy="11" r="11" fill="#fff"/><path d="M6 11 l3.5 3.5 l6.5 -7" stroke="#8b151b" stroke-width="2.6" fill="none"/></svg></li>
    <li>amet, consectetur adipiscing eli <svg width="22" height="22" viewBox="0 0 22 22"><circle cx="11" cy="11" r="11" fill="#fff"/><path d="M6 11 l3.5 3.5 l6.5 -7" stroke="#8b151b" stroke-width="2.6" fill="none"/></svg></li>
  </ul>
</section>

<section id="contact" class="contact-form">
  <h2 class="contact-title display">CONTACT US</h2>
  <p class="contact-sub">Call (555) 014-2290 or fill out the form below.</p>
  <div class="field" style="left:136px;top:2574px;width:309px;height:37px">Name</div>
  <div class="field" style="left:465px;top:2574px;width:281px;height:37px">Email</div>
  <div class="field" style="left:765px;top:2574px;width:299px;height:37px">Phone</div>
  <div class="field" style="left:136px;top:2631px;width:928px;height:107px;padding-top:14px">Message</div>
  <a class="btn" href="#">Contact us</a>
</section>

<div class="map" role="img" aria-label="Street map of the surrounding town with river and main roads"></div>

<footer class="footer">
  <div class="footer-brand">
    <div class="brand-mark"></div>
    <div class="brand-name">VALMIKE<br>GROUP</div>
  </div>
  <div class="footer-col" style="left:330px">
    <h4>SERVICES</h4>
    <ul><li>Executive Protection</li><li>Covert Protection</li><li>Residential Protection &amp; Intelligence</li></ul>
  </div>
  <div class="footer-col" style="left:597px">
    <h4>PAGES</h4>
    <ul><li>About Us</li><li>Services</li><li>Iron Finch</li><li>Contact Us</li></ul>
  </div>
  <div class="footer-col" style="left:752px">
    <h4>ABOUT US</h4>
    <ul><li>Company History</li><li>Our Team</li><li>Certifications</li><li>Careers</li><li>Sitemap</li></ul>
  </div>
  <div class="footer-col" style="left:908px">
    <h4>CONTACT</h4>
    <ul><li>&#9990; (555) 014-2290</li><li>&#9993; info@valmikegroup.com</li></ul>
  </div>
  <div class="social"><span></span><span></span><span></span></div>
</footer>
<div class="legal">Copyright © 2021 VALMIKE GROUP. All Rights Reserved</div>

</body>
</html>
```